Business Card Design

This is a card for a dental orthodontics(braces) clinic.we provide patients life changing experience by changing their smiles. Our clinic features state of the art technology . Our preferred color scheme is blue,green and purple.
Our target market is teens and adults

I have attached a logo, it can be modified in my chosen colors
Updates

Lpleaas keep in mind dr. Brisk is almost a fresh graduate and young, so the card should b fresh and vibrant

Reason: I have not received anything very satisfactory yet

• Dear all  the logo doesn't have to b something teeth related , it can b something based on simple lines like saome boxes etc

Industry/Entity Type

Dental

Contact Information for Business Card

HOLLOWAY.BRISK.
ORTHODONTICS

Oren Brisk, DDS, MS, MSD
Smile maker

Locations:
4815 N.Pelham Lane #142, Carrollton, TX 75061

6917 Meadow Ridge Drive #305, Plano, TX 75098

812 Larkspur, Seagoville, TX 75163

Phone:972-555-0148

```html
<!DOCTYPE html>
<html lang="en">
<head>
<meta charset="utf-8">
<title>Holloway Brisk Orthodontics – Business Card</title>
<link href="https://fonts.googleapis.com/css2?family=Exo+2:wght@400;600&display=swap" rel="stylesheet">
<style>
  :root {
    --bg: #e6e5e1;
    --card: #ffffff;
    --green-dark: #0f7a3a;
    --green: #1f8f3f;
    --green-light: #9ad33a;
    --ink: #3a3a3a;
    --grey: #8d8d8d;
    --icon: #a8a8a8;
  }
  * { margin: 0; padding: 0; box-sizing: border-box; }
  html, body { width: 1200px; height: 901px; overflow: hidden; }
  body {
    background: var(--bg);
    font-family: "Exo 2", sans-serif;
    position: relative;
  }
  .card {
    position: absolute;
    width: 560px;
    height: 320px;
    background: var(--card);
    box-shadow: 0 6px 18px rgba(0,0,0,.18);
    overflow: hidden;
  }
  .card--front { left: 320px; top: 80px; }
  .card--back { left: 320px; top: 480px; }
  .ribbons { position: absolute; inset: 0; }
  .brand {
    position: absolute;
    left: 0; right: 0;
    text-align: center;
    color: var(--green);
    font-weight: 600;
    letter-spacing: 2px;
    line-height: 1.25;
  }
  .brand__mark {
    display: block;
    width: 26px; height: 26px;
    border-radius: 50%;
    background: var(--green);
    margin: 0 auto 8px;
  }
  .brand__name { font-size: 19px; display: block; }
  .brand__sub { font-size: 11px; letter-spacing: 5px; display: block; }
  .card--front .brand { top: 110px; }
  .card--back .brand { top: 58px; }
  .person {
    position: absolute;
    left: 50px; top: 188px;
    color: var(--ink);
  }
  .person__name { font-size: 15px; font-weight: 600; letter-spacing: 1px; }
  .person__role { font-size: 9px; letter-spacing: 1px; margin-bottom: 8px; }
  .contact { list-style: none; font-size: 11px; color: var(--ink); }
  .contact li { display: flex; align-items: center; gap: 10px; margin-bottom: 6px; }
  .contact svg { width: 18px; height: 18px; flex: none; }
  .web { position: absolute; left: 360px; top: 150px; }
</style>
</head>
<body>

<section class="card card--front" aria-label="Card front">
  <svg class="ribbons" viewBox="0 0 560 320" aria-hidden="true">
    <defs>
      <linearGradient id="ribbonFront" x1="0" y1="0" x2="1" y2="0">
        <stop offset="0" stop-color="#0f7a3a"/>
        <stop offset=".55" stop-color="#9ad33a"/>
        <stop offset="1" stop-color="#0f7a3a"/>
      </linearGradient>
    </defs>
    <polygon points="0,105 150,28 230,28 205,46 230,62 190,62 0,150" fill="url(#ribbonFront)"/>
    <polygon points="385,0 440,0 560,88 560,138" fill="url(#ribbonFront)"/>
  </svg>
  <div class="brand">
    <span class="brand__mark"></span>
    <span class="brand__name">HOLLOWAY BRISK</span>
    <span class="brand__sub">ORTHODONTICS</span>
  </div>
</section>

<section class="card card--back" aria-label="Card back">
  <svg class="ribbons" viewBox="0 0 560 320" aria-hidden="true">
    <defs>
      <linearGradient id="ribbonBack" x1="0" y1="0" x2="1" y2="0">
        <stop offset="0" stop-color="#0f7a3a"/>
        <stop offset=".55" stop-color="#9ad33a"/>
        <stop offset="1" stop-color="#0f7a3a"/>
      </linearGradient>
    </defs>
    <polygon points="0,165 135,40 190,40 0,230" fill="url(#ribbonBack)"/>
    <polygon points="300,8 480,8 560,60 560,100 470,42 300,42 322,25" fill="url(#ribbonBack)"/>
  </svg>

  <div class="brand">
    <span class="brand__mark"></span>
    <span class="brand__name">HOLLOWAY BRISK</span>
    <span class="brand__sub">ORTHODONTICS</span>
  </div>

  <div class="person">
    <p class="person__name">DANIEL MERCER</p>
    <p class="person__role">FINANCIAL ADVISOR</p>
    <ul class="contact">
      <li>
        <svg viewBox="0 0 18 18"><rect width="18" height="18" rx="2" fill="var(--icon)"/><path d="M9 4a3 3 0 0 0-3 3c0 2.3 3 6 3 6s3-3.7 3-6a3 3 0 0 0-3-3z" fill="#fff"/><circle cx="9" cy="7" r="1" fill="var(--icon)"/></svg>
        Street country,123
      </li>
      <li>
        <svg viewBox="0 0 18 18"><rect width="18" height="18" rx="2" fill="var(--icon)"/><path d="M6 4l2 2-1 1.5c.6 1.4 1.6 2.4 3 3L11.5 9.5l2 2-1.5 1.5C8.5 13 5 9.5 4.5 6z" fill="#fff"/></svg>
        012 345 6789
      </li>
      <li>
        <svg viewBox="0 0 18 18"><rect width="18" height="18" rx="2" fill="var(--icon)"/><rect x="4" y="5.5" width="10" height="7" fill="#fff"/><path d="M4 5.5l5 4 5-4" fill="none" stroke="var(--icon)"/></svg>
        urname@email.com
      </li>
    </ul>
  </div>

  <ul class="contact web">
    <li>
      <svg viewBox="0 0 18 18"><rect width="18" height="18" rx="2" fill="var(--icon)"/><circle cx="9" cy="9" r="4.5" fill="none" stroke="#fff" stroke-width="1.4"/></svg>
      www.urwebsitename.com
    </li>
    <li>
      <svg viewBox="0 0 18 18"><rect width="18" height="18" rx="2" fill="var(--icon)"/><rect x="6" y="6" width="6" height="6" fill="#fff"/></svg>
      www.chirpline.com
    </li>
    <li>
      <svg viewBox="0 0 18 18"><rect width="18" height="18" rx="2" fill="var(--icon)"/><rect x="6" y="6" width="6" height="6" fill="#fff"/></svg>
      www.friendpage.com
    </li>
  </ul>
</section>

</body>
</html>
```